Private Security Company Business Card and Logo Design

Looking for a modern conservative business card design for our new private security company Harbor Ridge Guard Co., Inc. or HRGC for short.
Private Security Services. The current logo we have is not very good and honestly would like a sharp logo for the card instead of using the one we have now. Open to ideas. I am easy just looking for something nicer then what I can personally design on cardmillo. I searched on zintoo for Security Company business cards went to images and found some nice designs that were made here.

Target Market(s)

Security Services

Industry/Entity Type

Business

Contact Information for Business Card

Harbor Ridge Guard Co., Inc.
President, cell,office,fax,email, website,
Logo etc, whatever is needed for a standard business card
Can provide personal Information later.

Colors
0556a4
ffffff
474747

Requirements
Must have
• Modern but conservative,
Nice to have
• color choices
• Blue, white, Grey

```html
<!DOCTYPE html>
<html lang="en">
<head>
<meta charset="utf-8">
<title>Harbor Ridge Guard Co., Inc. – Business Card</title>
<link rel="stylesheet" href="https://fonts.googleapis.com/css2?family=Michroma&family=Open+Sans:ital,wght@0,400;1,400&display=swap">
<style>
  :root {
    --page: #ffffff;
    --card: #020c16;
    --card-edge: #0a1622;
    --silver: #b9bfc6;
    --text-light: #e6e8ea;
    --text-soft: #d2d6da;
    --brand-blue: #0556a4;
    --shadow: rgba(0, 0, 0, 0.45);
  }
  * { box-sizing: border-box; margin: 0; padding: 0; }
  html, body {
    width: 1014px;
    height: 1200px;
    overflow: hidden;
    background: var(--page);
  }
  .sheet {
    position: relative;
    width: 1014px;
    height: 1200px;
  }
  .card {
    position: absolute;
    left: 9px;
    width: 980px;
    height: 570px;
    background: var(--card);
    border: 1px solid var(--card-edge);
    box-shadow: 4px 5px 8px var(--shadow);
    overflow: hidden;
  }
  .card--front { top: 9px; }
  .card--back { top: 603px; }

  .brand-mark {
    position: absolute;
    display: flex;
    align-items: center;
    gap: 14px;
  }
  .brand-mark__dot {
    width: 44px;
    height: 44px;
    border-radius: 50%;
    background: var(--brand-blue);
  }
  .brand-mark__name {
    font-family: "Michroma", sans-serif;
    color: var(--silver);
    font-size: 38px;
    letter-spacing: 2px;
  }
  .card--front .brand-mark { left: 40px; top: 100px; }
  .card--back .brand-mark {
    left: 50%;
    top: 230px;
    transform: translateX(-50%);
  }
  .card--back .brand-mark__dot { width: 64px; height: 64px; }
  .card--back .brand-mark__name { font-size: 56px; }

  .company-name {
    position: absolute;
    font-family: "Michroma", sans-serif;
    font-weight: 400;
    color: var(--silver);
    white-space: nowrap;
  }
  .card--front .company-name {
    right: 34px;
    top: 128px;
    font-size: 26px;
    letter-spacing: 0.5px;
  }
  .card--back .company-name {
    left: 0;
    right: 0;
    top: 378px;
    text-align: center;
    font-size: 34px;
    letter-spacing: 0.5px;
  }

  .person {
    position: absolute;
    left: 0;
    width: 980px;
    top: 245px;
    text-align: center;
    font-family: "Open Sans", sans-serif;
    color: var(--text-light);
  }
  .person__name {
    font-size: 38px;
    font-variant: small-caps;
    line-height: 1.15;
    margin-left: -14px;
  }
  .person__title {
    font-size: 32px;
    font-style: italic;
    line-height: 1.3;
    margin-left: -14px;
  }

  .contact {
    position: absolute;
    top: 434px;
    font-family: "Open Sans", sans-serif;
    color: var(--text-soft);
  }
  .contact--phones { left: 56px; font-size: 30px; }
  .contact--web { right: 34px; text-align: right; }
  .contact__line {
    display: flex;
    align-items: center;
    gap: 8px;
    height: 44px;
    white-space: nowrap;
  }
  .contact--web .contact__line { justify-content: flex-end; }
  .contact__icon { width: 26px; height: 26px; fill: var(--text-soft); }
  .contact__site { font-size: 30px; }
  .contact__address { font-size: 27px; font-style: italic; }
</style>
</head>
<body>
<main class="sheet">
  <section class="card card--front" aria-label="Card front">
    <div class="brand-mark">
      <span class="brand-mark__dot"></span>
      <span class="brand-mark__name">HRGC</span>
    </div>
    <h1 class="company-name">HARBOR RIDGE GUARD CO., INC.</h1>

    <div class="person">
      <p class="person__name">Dana Whitfield</p>
      <p class="person__title">President</p>
    </div>

    <div class="contact contact--phones">
      <p class="contact__line">
        <svg class="contact__icon" viewBox="0 0 26 26" aria-label="Phone">
          <path d="M2 9c0-3 5-5 11-5s11 2 11 5v2h-6V9c-2-1-8-1-10 0v2H2z"/>
          <path d="M7 13h12l3 9H4z"/>
        </svg>
        <span>(555) 284-3190</span>
      </p>
      <p class="contact__line">
        <svg class="contact__icon" viewBox="0 0 26 26" aria-label="Fax">
          <rect x="7" y="2" width="12" height="8"/>
          <rect x="3" y="11" width="20" height="12" rx="1"/>
          <rect x="6" y="14" width="3" height="2" fill="#020c16"/>
          <rect x="11" y="14" width="3" height="2" fill="#020c16"/>
          <rect x="6" y="18" width="3" height="2" fill="#020c16"/>
          <rect x="11" y="18" width="3" height="2" fill="#020c16"/>
        </svg>
        <span>(555) 284-3191</span>
      </p>
    </div>

    <div class="contact contact--web">
      <p class="contact__line contact__site">www.harborridgeguard.com</p>
      <p class="contact__line contact__address">42 Pier Lane, Bayport, ME 04021</p>
    </div>
  </section>

  <section class="card card--back" aria-label="Card back">
    <div class="brand-mark">
      <span class="brand-mark__dot"></span>
      <span class="brand-mark__name">HRGC</span>
    </div>
    <p class="company-name">HARBOR RIDGE GUARD CO., INC.</p>
  </section>
</main>
</body>
</html>
```